Copperleaf Vantage Training PowerPoint Template

I want to PowerPoint template theme using my attached logo. My colors are black and orange. My website is CopperleafVantage.com. I am a handgun training company.

Font:

- Serpentine-Bold-Bold for "IRON BRAE"

- BrowalliaUPC for "SHOOTING SPORTS"

Colors (CMYK code):

- BLACK ....... 0; 0; 0; 100;
- ORANGE ... gradient from 0; 65; 97.5; 0 to 0; 39; 97.5; 0

```html
<!DOCTYPE html>
<html lang="en">
<head>
<meta charset="utf-8">
<title>Iron Brae Shooting Sports – Title Slide</title>
<link rel="stylesheet" href="https://fonts.googleapis.com/css2?family=Russo+One&family=Arimo:wght@400;700&display=swap">
<style>
  :root {
    --orange-deep: #ee7d1c;
    --orange-gold: #e9b800;
    --black: #000000;
    --slide-dark: #0c0c0c;
    --slide-mid: #1a1a1a;
    --steel-light: #d9d9d9;
    --steel-dark: #7a7a7a;
    --accent-yellow: #e8b400;
    --white: #ffffff;
    --ink: #111111;
  }
  * { margin: 0; padding: 0; box-sizing: border-box; }
  html, body { width: 1200px; height: 900px; overflow: hidden; background: var(--black); }
  .slide {
    position: relative;
    width: 1200px;
    height: 900px;
    overflow: hidden;
    font-family: "Arimo", Arial, sans-serif;
    background: radial-gradient(ellipse at 50% 55%, var(--slide-mid) 0%, var(--slide-dark) 70%);
  }
  .band {
    position: absolute;
    left: 0;
    width: 100%;
    background: linear-gradient(90deg, var(--orange-deep) 0%, var(--orange-gold) 40%, var(--orange-gold) 60%, var(--orange-deep) 100%);
  }
  .band--top { top: 0; height: 182px; }
  .band--bottom { top: 806px; height: 94px; }
  .rule {
    position: absolute;
    left: 0;
    width: 100%;
    height: 6px;
    background: linear-gradient(90deg, var(--steel-dark), var(--steel-light) 50%, var(--steel-dark));
  }
  .rule--top { top: 182px; }
  .rule--bottom { top: 800px; }

  .brand-mark {
    position: absolute;
    left: 52px;
    top: 46px;
    width: 160px;
    display: flex;
    flex-direction: column;
    align-items: center;
    gap: 8px;
  }
  .brand-mark__dot {
    width: 34px;
    height: 34px;
    border-radius: 50%;
    background: var(--ink);
  }
  .brand-mark__name {
    font-family: "Arimo", Arial, sans-serif;
    font-weight: 700;
    font-size: 17px;
    line-height: 1.15;
    text-align: center;
    color: var(--ink);
    text-transform: uppercase;
  }

  .header-title {
    position: absolute;
    left: 258px;
    top: 62px;
    display: flex;
    align-items: baseline;
    gap: 34px;
    white-space: nowrap;
    color: var(--ink);
  }
  .header-title__team {
    font-family: "Russo One", Arial, sans-serif;
    font-size: 48px;
    letter-spacing: 1px;
  }
  .header-title__sport {
    font-family: "Arimo", Arial, sans-serif;
    font-size: 44px;
    font-weight: 400;
    letter-spacing: 1px;
  }

  .title {
    position: absolute;
    left: 0;
    width: 100%;
    top: 320px;
    text-align: center;
    font-family: "Russo One", Arial, sans-serif;
    font-size: 63px;
    letter-spacing: 2px;
    color: var(--accent-yellow);
  }
  .subtitle {
    position: absolute;
    left: 0;
    width: 100%;
    top: 463px;
    text-align: center;
    font-size: 40px;
    color: var(--white);
  }
  .presenter {
    position: absolute;
    left: 426px;
    width: 400px;
    top: 655px;
    text-align: center;
    font-size: 26px;
    line-height: 35px;
    color: var(--accent-yellow);
  }
  .presenter__name { font-weight: 700; }

  .site-url {
    position: absolute;
    left: 0;
    width: 100%;
    top: 829px;
    text-align: center;
    font-size: 35px;
    color: var(--ink);
  }
</style>
</head>
<body>
  <main class="slide">
    <header>
      <div class="band band--top"></div>
      <div class="rule rule--top"></div>
      <div class="brand-mark">
        <span class="brand-mark__dot"></span>
        <span class="brand-mark__name">Copperleaf Vantage Training</span>
      </div>
      <h1 class="header-title">
        <span class="header-title__team">IRON BRAE</span>
        <span class="header-title__sport">SHOOTING SPORTS</span>
      </h1>
    </header>

    <section>
      <h2 class="title">PRESENTATION TITLE</h2>
      <p class="subtitle">Presentation Subtitle</p>
      <div class="presenter">
        <p class="presenter__date">February 2014</p>
        <p class="presenter__name">PRESENTOR’S NAME</p>
        <p class="presenter__role">Job Title</p>
      </div>
    </section>

    <footer>
      <div class="rule rule--bottom"></div>
      <div class="band band--bottom"></div>
      <p class="site-url">www.copperleafvantage.com</p>
    </footer>
  </main>
</body>
</html>
```